Brochure Design Project for Folk High School in Norway

We're a Folk High School placed in the south of Norway. We want help in creating a new brochure for our school next year. Check this link for the brochure for current year: http://www.brennvikskole.no/db/repository/x58301746290385716204937.pdf

We want a new design. It should not be larger than A4 size. The design dosen't need to be quadratic.

As a starting, the borchure should contain the same amount of pages and information as current brochure.

We also want access to the working-file (InDesign). We've got a lot of pictures to use, so the design template could contain more pictures.

This is a School for students in the agegroup between 18-20 years. The design must attract this group. It's a 1-year study and our focus is to give the students qualified teaching in their area of interest and great experiences linked to travelling, friendship and personal development.

As a starter, we want to see a template on a modern, playful,warm and attractive brochure. This could be shown as a PDF-file.
Updates

You can follow this link to choose among several pictures:

http://www.pixmora.example/photos/41572038@N09/

I remind you that we want access to de InDesign file... So the choose of pictures is not that important. We want for ourselves to change them. If you follow the link, you''ll find compressed pictures. But maybe they can help you in the creative process... :) We''re looking forward to see your work!

```html
<!DOCTYPE html>
<html lang="no">
<head>
<meta charset="utf-8">
<title>Mer enn skole – brosjyreoppslag</title>
<link rel="stylesheet" href="https://fonts.googleapis.com/css2?family=Noto+Sans:wght@400;700&family=Gochi+Hand&display=swap">
<style>
  :root {
    --page: #e4e4e4;
    --red: #c8363b;
    --slate: #4a4a4a;
    --ink: #1e1e1e;
    --light: #ffffff;
    --mist-1: #f4f4f4;
    --mist-2: #d6d6d6;
    --stage-1: #1a1a22;
    --stage-2: #3c2a40;
    --stage-3: #2c3f78;
  }
  * { box-sizing: border-box; margin: 0; padding: 0; }
  html, body { width: 1200px; height: 939px; overflow: hidden; background: var(--page); }
  .spread {
    position: relative; width: 1200px; height: 939px;
    font-family: "Noto Sans", Verdana, sans-serif; color: var(--ink);
  }
  .band-red { position: absolute; left: 26px; top: 26px; width: 231px; height: 887px; background: var(--red); }
  .band-slate { position: absolute; left: 257px; top: 26px; width: 115px; height: 887px; background: var(--slate); }
  .title {
    position: absolute; left: 142px; top: 522px;
    transform: translate(-50%, -50%) rotate(-90deg);
    font-family: "Gochi Hand", cursive; font-size: 50px; color: var(--light);
    white-space: nowrap; letter-spacing: 1px;
  }
  .mist {
    position: absolute; left: 372px; top: 26px; width: 802px; height: 713px;
    background: radial-gradient(ellipse at 30% 40%, var(--mist-1), transparent 60%),
                radial-gradient(ellipse at 75% 65%, var(--mist-1), transparent 55%),
                linear-gradient(160deg, var(--mist-2), #eaeaea 50%, var(--mist-2));
  }
  .photo {
    position: absolute; left: 372px; top: 739px; width: 802px; height: 174px;
    background: radial-gradient(ellipse at 55% 30%, var(--stage-3), transparent 45%),
                radial-gradient(ellipse at 20% 70%, var(--stage-2), transparent 50%),
                linear-gradient(90deg, var(--stage-1), #2a2230 50%, var(--stage-1));
  }
  .column { position: absolute; top: 139px; font-size: 10.5px; line-height: 1.4; }
  .column.left { left: 435px; width: 305px; }
  .column.right { left: 783px; width: 260px; }
  .intro { font-weight: 700; margin-bottom: 15px; }
  .item { margin-bottom: 14px; padding-left: 12px; text-indent: -12px; }
  .item b { font-weight: 700; }
</style>
</head>
<body>
<div class="spread">
  <div class="band-red"></div>
  <div class="band-slate"></div>
  <div class="title">Mer enn skole</div>
  <div class="mist"></div>
  <div class="photo" role="img" aria-label="Elever som danser på en scene under blått og rødt scenelys"></div>

  <div class="column left">
    <p class="intro">Vi har fryktelig lyst til at nettopp du skal komme på vår skole til neste år! Hvorfor? Vi tror at DU sammen med OSS kan bli fantastiske! Vi er sikre på at vi kan tilby noe helt spesielt til deg. Et år sammen med oss blir dynamitt! Det er nemlig noen ting som er litt kjipt å ikke få med seg:</p>
    <p class="item">• <b>Venner for livet.</b> Bli kjent med elever fra hele landet! – Og ikke minst elevene på internasjonal linje!</p>
    <p class="item">• <b>Ekskursjoner</b> og opplevelser kun en folkehøgskole kan gi. Ecuador, Uganda, Budapest eller Hovden kan bli ditt reisemål til neste år!</p>
    <p class="item">• <b>Sosiale kvelder</b> i TV-stua. Slapp av med en god TV-serie eller et slag kortkaos på kalde høstkvelder.</p>
    <p class="item">• <b>Gymsal, svømmebasseng og treningsstudio</b> tilgjengelig hver dag.</p>
    <p class="item">• <b>Vårskolehagen</b> leden av å gi deg lunsj hver dag. – det er vi stolte over! I blant også varm lunsj.</p>
    <p class="item">• <b>Utflukter</b> i og rundt Sørlandet. Opplev Julius, Flekkeløner, Havgløt, Hamresanden, Skagerøya og mye mer.</p>
    <p class="item">• <b>Velg et</b> år hvor du kan bli enda bedre i det du allerede er flink til!</p>
    <p class="item">• <b>Finn ut</b> hva du skal bli! Vi har elevveiledere som kan hjelpe deg med å stille de rette spørsmålene.</p>
  </div>

  <div class="column right">
    <p class="item">• <b>Quizkvelder, elevkvelder, spillkvelder og filmkvelder.</b> Det burde interessere noen og enhver..</p>
    <p class="item">• <b>Chille sammen</b> med venner rundt et slag med biljard. Slå knockout på kompisen din i bordtennis</p>
    <p class="item">• <b>Mekke</b> på bilen i bilverkstedet. Vi har løftebukker og stor garasje!</p>
    <p class="item">• <b>Turløyper</b> i nærområdet for trening sommer og vinter. Hold kroppen i form!</p>
    <p class="item">• <b>Musikal.</b> Hele skolen setter opp egenprodusert musikal. Dette er veldig gøy!</p>
    <p class="item">• <b>Fiber</b> på rommet gjør det mulig å være online..</p>
    <p class="item">• <b>Møter</b> på kveldstid hvor troen din kan bli inspirert og kanskje utfordret.</p>
    <p class="item">• <b>Bli medlem og støtt</b> internasjonale prosjekter og bidra til en mer rettferdig verden. Skolen har flere bistandsprosjekter som du blir godt kjent med. – opplev hva din innsats betyr.</p>
    <p class="item">• <b>Danmark.</b> Hele skolen reiser på bli-veldig-godt-kjent-tur til Danmark. Tre-firedager i landet hvor det er deilig å være norsk!</p>
  </div>
</div>
</body>
</html>
```